Driftwood Coatings of Central Florida, LLC. Start-up painting business needs a professional web desig

We have a start up painting business that would like to reach/focus on commercial clients like building contractors, HOA's, apartment complexes, etc.. We would like a residential aspect to the web design as well. We have an existing website at "trydriftwoodcoatings.com" with usable content. Have logo and color scheme attached. Use provided website ONLY as template. Add commercial services page. Can type own content when needed.

```html
<!DOCTYPE html>
<html lang="en">
<head>
<meta charset="utf-8">
<title>Driftwood Coatings of Central Florida, LLC</title>
<link href="https://fonts.googleapis.com/css2?family=Open+Sans:wght@400;600;700&family=Roboto:wght@400;500;700&display=swap" rel="stylesheet">
<style>
:root{
  --peach:#fbe6d3;
  --orange:#f29a1c;
  --amber:#fdb515;
  --green:#7fb81c;
  --lime:#8dc21f;
  --ink:#3a3a3a;
  --muted:#8a8a8a;
  --nav:#8e8e8e;
  --footer:#737373;
  --footer-dark:#5d5d5d;
  --olive:#6c6b45;
  --card:#f7f7f7;
  --white:#ffffff;
}
*{box-sizing:border-box;margin:0;padding:0}
html,body{width:1200px;height:2400px;overflow:hidden;background:var(--peach)}
body{font-family:"Roboto",Arial,sans-serif;color:var(--ink)}
.page{position:relative;width:1200px;height:2400px;overflow:hidden;background:var(--peach)}
.abs{position:absolute}
ul{list-style:none}

/* header */
.masthead{left:0;top:0;width:1200px;height:125px;background:var(--nav)}
.brand{left:0;top:0;width:490px;height:125px;background:linear-gradient(#fafafa,#e6e6e6);display:flex;align-items:center;gap:18px;padding-left:22px}
.brand-mark{width:80px;height:80px;border-radius:50%;background:var(--orange);flex:none}
.brand-name{font-family:"Roboto",Arial,sans-serif;font-weight:700;color:var(--orange);font-size:25px;line-height:31px;text-transform:uppercase}
.main-nav{left:515px;top:46px;display:flex;gap:34px;font-family:"Open Sans",Arial,sans-serif;font-size:17px;font-weight:600;color:#e8e8e8;text-transform:uppercase}
.main-nav .current{color:var(--white);font-weight:700}

/* slider */
.slider{left:0;top:128px;width:1200px;height:408px;border:6px solid var(--lime);background:linear-gradient(90deg,#f4f4f4 0%,#dcdcdc 45%,#6f6f6f 60%,#8a8a8a 100%)}
.slider-glow{left:40px;top:536px;width:1120px;height:12px;background:radial-gradient(ellipse at center,rgba(141,194,31,.55),rgba(141,194,31,0) 70%)}
.slide-arrow{top:298px;width:66px;height:66px;border-radius:50%;background:#3c3c3c;border:3px solid #fff}
.slide-arrow svg{position:absolute;left:18px;top:18px}
.prev{left:-34px}.next{right:-34px;background:#f2f2f2;border-color:#333}
.next svg{left:8px}
.dots{left:86px;top:474px;display:flex;gap:10px}
.dots span{width:13px;height:13px;border-radius:50%;background:#bdbdbd}
.dots span:first-child{background:#555}

/* features */
.feature{top:575px;width:370px;text-align:center}
.feature-photo{width:250px;height:250px;margin:0 auto;border-radius:50%;border:8px solid #fff;box-shadow:0 2px 10px rgba(0,0,0,.25)}
.feature h2{margin-top:20px;font-weight:500;color:var(--green);font-size:25px}
.feature p{margin-top:6px;text-align:left;font-size:14px;line-height:17px;font-weight:700;color:#3d3d3d}

/* why choose */
.why{left:55px;top:1038px;width:360px}
.why h2{font-family:"Open Sans",Arial,sans-serif;color:var(--orange);font-size:27px;font-weight:700}
.why li{display:flex;align-items:center;gap:16px;height:35px;font-size:14px;color:#444}
.why ul{margin-top:24px}
.bullet{width:24px;height:24px;border-radius:50%;background:var(--olive);flex:none;display:flex;align-items:center;justify-content:center}
.perk{width:302px;height:112px;background:var(--card);border-radius:10px;box-shadow:0 1px 3px rgba(0,0,0,.06);padding:12px 14px}
.perk-icon{position:absolute;left:14px;top:28px;width:60px;height:60px;border-radius:50%;background:var(--amber);display:flex;align-items:center;justify-content:center}
.perk h3{margin-left:74px;text-align:center;font-size:27px;font-weight:500;color:var(--orange);text-transform:uppercase;line-height:30px}
.perk p{margin-left:76px;margin-top:4px;font-size:14px;line-height:16px;color:#444}

/* columns */
.rule{left:44px;top:1343px;width:1112px;height:1px;background:#e8cbb0}
.col-title{font-family:"Open Sans",Arial,sans-serif;font-size:18px;font-weight:700;color:var(--orange);text-transform:uppercase}
.services{left:48px;top:1368px;width:262px}
.services ul{margin-top:20px}
.services li{display:flex;align-items:center;gap:14px;height:35px;border-bottom:1px solid #efd4ba;font-size:14px;font-weight:500;color:#222}
.btn{display:inline-block;width:108px;height:30px;line-height:30px;border-radius:15px;background:var(--orange);color:#fff;font-family:"Open Sans",Arial,sans-serif;font-weight:700;font-size:15px;text-align:center;box-shadow:0 2px 0 #c87a10}
.blog{left:340px;top:1368px;width:260px}
.blog-photo{margin-top:24px;width:242px;height:94px;border:3px solid #fff;background:linear-gradient(90deg,#6a3f8a,#d8436b,#f5a623,#2aa4c8,#4a5fb5)}
.blog h3{margin-top:18px;font-size:20px;font-weight:400;color:var(--orange);line-height:24px}
.blog p{margin-top:6px;font-size:15px;line-height:20px;color:#222}
.tweets{left:915px;top:1368px;width:250px}
.tweets ul{margin-top:22px}
.tweets li{position:relative;padding-left:34px;margin-bottom:18px;font-size:14px;line-height:20px;color:#9a9a9a}
.tweets li::before{content:"";position:absolute;left:0;top:4px;width:16px;height:16px;border-radius:50%;background:#e8866a}
.tweets .link{display:block;margin-top:8px;color:#222;font-style:italic}

/* support bar */
.support{left:12px;top:1814px;width:1176px;height:70px;border-radius:10px;background:var(--amber);box-shadow:0 2px 4px rgba(0,0,0,.25);color:#fff;font-family:"Open Sans",Arial,sans-serif;font-size:36px;font-weight:600;text-align:center;line-height:70px}

/* footer */
.footer{left:0;top:1900px;width:1200px;height:370px;background:var(--footer)}
.f-col{top:50px}
.f-col h4{font-family:"Open Sans",Arial,sans-serif;font-size:14px;font-weight:700;color:#fff;text-transform:uppercase}
.f-about{left:48px;width:250px}
.f-about p{margin-top:22px;font-size:14px;line-height:20px;color:#c9c9c9}
.f-news{left:336px;width:250px}
.f-news ul{margin-top:14px}
.f-news li{display:flex;gap:12px;align-items:center;height:35px;border-bottom:1px solid #828282;font-size:14px;color:#eee}
.f-news li.hot{color:#c7e35a}
.f-posts{left:626px;width:260px}
.f-post{display:flex;gap:14px;margin-top:18px;height:60px}
.thumb{width:58px;height:44px;background:#686868;border:1px solid #7e7e7e;display:flex;align-items:center;justify-content:center;flex:none}
.f-post p{font-size:14px;line-height:18px;color:#eee}
.f-post p.hot{color:#c7e35a}
.f-post em{display:block;color:#c9c9c9}
.f-contact{left:910px;width:242px}
.field{margin-top:12px;width:240px;height:38px;border-radius:6px;background:#8b8b8b;border:1px solid #7a7a7a;padding:0 14px;line-height:38px;font-size:13px;color:#cfcfcf;text-transform:uppercase}
.f-contact .first{margin-top:20px}
.field.msg{height:86px}
.send{margin-top:12px;width:110px;height:28px;border-radius:14px;background:linear-gradient(#4a4a4a,#2e2e2e);border:2px solid #bbb;color:#fff;text-align:center;font-size:14px;font-weight:700;line-height:24px}
.social-bar{left:0;top:2270px;width:1200px;height:76px;background:var(--footer-dark)}
.social-bar h4{position:absolute;left:48px;top:26px;font-family:"Open Sans",Arial,sans-serif;font-size:17px;font-weight:600;color:#fff;text-transform:uppercase}
.socials{position:absolute;right:48px;top:22px;display:flex;gap:26px;align-items:center;font-size:14px;color:#eee}
.socials span{display:flex;align-items:center;gap:10px}
.socials i{width:28px;height:28px;border-radius:50%;background:#e9e9e9;display:block}
.copyright{left:0;top:2346px;width:1200px;height:54px;background:var(--footer);text-align:center;line-height:54px;font-size:13px;color:#a6a6a6}
</style>
</head>
<body>
<div class="page">

  <header class="abs masthead">
    <div class="abs brand">
      <span class="brand-mark"></span>
      <span class="brand-name">Driftwood Coatings of<br>Central Florida, LLC.</span>
    </div>
    <nav class="abs main-nav">
      <span class="current">Home</span><span>About Us</span><span>Commercial Services</span><span>Projects</span><span>Contact Us</span>
    </nav>
  </header>

  <section class="abs slider" role="img" aria-label="Photo of a bright modern office interior with white desks and orange wall cabinets"></section>
  <div class="abs slider-glow"></div>
  <div class="abs slide-arrow prev"><svg width="26" height="26" viewBox="0 0 26 26"><path d="M12 5 4 13l8 8M21 5l-8 8 8 8" fill="none" stroke="#fff" stroke-width="3"/></svg></div>
  <div class="abs slide-arrow next"><svg width="26" height="26" viewBox="0 0 26 26"><path d="M5 5l8 8-8 8M14 5l8 8-8 8" fill="none" stroke="#333" stroke-width="3"/></svg></div>
  <div class="abs dots"><span></span><span></span><span></span><span></span></div>

  <section class="abs feature" style="left:32px">
    <div class="feature-photo" role="img" aria-label="Spiral of rainbow coloured paper fans" style="background:conic-gradient(#e53935,#fb8c00,#fdd835,#43a047,#1e88e5,#8e24aa,#e53935)"></div>
    <h2>Great Flexibility</h2>
    <p>Lorem ipsum dolor sit amet, consectetur adipiscing elit. Morbi velit diam, euismod eget rhoncus in, tincidunt pulvinar ligula. Praesent ipsum mi, consectetur ut aliquet ac, pulvinar eu risus.</p>
  </section>
  <section class="abs feature" style="left:415px">
    <div class="feature-photo" role="img" aria-label="Open paint cans with a colour swatch fan" style="background:radial-gradient(circle at 50% 40%,#e0e0e0,#b0b0b0 55%,#f0c040 80%,#4caf50)"></div>
    <h2>Creative and clean design</h2>
    <p>Lorem ipsum dolor sit amet, consectetur adipiscing elit. Morbi velit diam, euismod eget rhoncus in, tincidunt pulvinar ligula. Praesent ipsum mi, consectetur ut aliquet ac, pulvinar eu risus.</p>
  </section>
  <section class="abs feature" style="left:802px">
    <div class="feature-photo" role="img" aria-label="Splashes of bright paint on a black background" style="background:radial-gradient(circle at 50% 55%,#e91e63 0%,#7b1fa2 20%,#1565c0 35%,#111 60%)"></div>
    <h2>Easy SiteDesk edit</h2>
    <p>Lorem ipsum dolor sit amet, consectetur adipiscing elit. Morbi velit diam, euismod eget rhoncus in, tincidunt pulvinar ligula. Praesent ipsum mi, consectetur ut aliquet ac, pulvinar eu risus.</p>
  </section>

  <section class="abs why">
    <h2>Why choose us ?</h2>
    <ul>
      <li><span class="bullet"><svg width="12" height="12" viewBox="0 0 12 12"><path d="M2 2l4 4-4 4M6 2l4 4-4 4" fill="none" stroke="#fff" stroke-width="1.8"/></svg></span>Lorem ipsum dolor sit amet, consectetur.</li>
      <li><span class="bullet"><svg width="12" height="12" viewBox="0 0 12 12"><path d="M2 2l4 4-4 4M6 2l4 4-4 4" fill="none" stroke="#fff" stroke-width="1.8"/></svg></span>Ipsum dolor sit amet, consectetur.</li>
      <li><span class="bullet"><svg width="12" height="12" viewBox="0 0 12 12"><path d="M2 2l4 4-4 4M6 2l4 4-4 4" fill="none" stroke="#fff" stroke-width="1.8"/></svg></span>Lorem ipsum dolor sit amet, consectetur.</li>
      <li><span class="bullet"><svg width="12" height="12" viewBox="0 0 12 12"><path d="M2 2l4 4-4 4M6 2l4 4-4 4" fill="none" stroke="#fff" stroke-width="1.8"/></svg></span>Dolor sit amet, consectetur.</li>
      <li><span class="bullet"><svg width="12" height="12" viewBox="0 0 12 12"><path d="M2 2l4 4-4 4M6 2l4 4-4 4" fill="none" stroke="#fff" stroke-width="1.8"/></svg></span>Lorem ipsum dolor sit amet.</li>
    </ul>
  </section>

  <div class="abs perk" style="left:458px;top:1048px">
    <span class="perk-icon"><svg width="28" height="24" viewBox="0 0 28 24"><rect x="2" y="2" width="24" height="16" rx="2" fill="none" stroke="#fff" stroke-width="2.5"/><path d="M10 22h8" stroke="#fff" stroke-width="2.5"/></svg></span>
    <h3>Gallery</h3><p>Lorem ipsum dolor sit amet, consectetur adipiscing elit. Morbi velit diam.</p>
  </div>
  <div class="abs perk" style="left:815px;top:1048px">
    <span class="perk-icon"><svg width="28" height="26" viewBox="0 0 28 26"><path d="M3 3h22v15H11l-6 5v-5H3z" fill="none" stroke="#fff" stroke-width="2.5" stroke-linejoin="round"/></svg></span>
    <h3>Featured</h3><p>Lorem ipsum dolor sit amet, consectetur adipiscing elit. Morbi velit diam.</p>
  </div>
  <div class="abs perk" style="left:458px;top:1175px">
    <span class="perk-icon"><svg width="24" height="28" viewBox="0 0 24 28"><path d="M3 2h13l5 5v19H3z" fill="none" stroke="#fff" stroke-width="2.5" stroke-linejoin="round"/></svg></span>
    <h3>Commercial</h3><p>Lorem ipsum dolor sit amet, consectetur adipiscing elit. Morbi velit diam.</p>
  </div>
  <div class="abs perk" style="left:815px;top:1175px">
    <span class="perk-icon"><svg width="28" height="24" viewBox="0 0 28 24"><rect x="2" y="3" width="24" height="18" rx="2" fill="none" stroke="#fff" stroke-width="2.5"/><path d="M3 5l11 9 11-9" fill="none" stroke="#fff" stroke-width="2.5"/></svg></span>
    <h3>Great Support</h3><p>Lorem ipsum dolor sit amet, consectetur adipiscing elit. Morbi velit diam.</p>
  </div>

  <div class="abs rule"></div>

  <section class="abs services">
    <h3 class="col-title">Our Services</h3>
    <ul>
      <li><svg width="10" height="10" viewBox="0 0 10 10"><path d="M1 1l4 4-4 4M5 1l4 4-4 4" fill="none" stroke="#333" stroke-width="1.4"/></svg>Lorem ipsum dolor sit amet</li>
      <li><svg width="10" height="10" viewBox="0 0 10 10"><path d="M1 1l4 4-4 4M5 1l4 4-4 4" fill="none" stroke="#333" stroke-width="1.4"/></svg>Sed ornare sodales purus</li>
      <li><svg width="10" height="10" viewBox="0 0 10 10"><path d="M1 1l4 4-4 4M5 1l4 4-4 4" fill="none" stroke="#333" stroke-width="1.4"/></svg>Morbi et purus sed dolor</li>
      <li><svg width="10" height="10" viewBox="0 0 10 10"><path d="M1 1l4 4-4 4M5 1l4 4-4 4" fill="none" stroke="#333" stroke-width="1.4"/></svg>In hac habitasse platea dictumst</li>
      <li><svg width="10" height="10" viewBox="0 0 10 10"><path d="M1 1l4 4-4 4M5 1l4 4-4 4" fill="none" stroke="#333" stroke-width="1.4"/></svg>Pellentesque turpis eros</li>
      <li><svg width="10" height="10" viewBox="0 0 10 10"><path d="M1 1l4 4-4 4M5 1l4 4-4 4" fill="none" stroke="#333" stroke-width="1.4"/></svg>In egestas posuere ipsum</li>
      <li><svg width="10" height="10" viewBox="0 0 10 10"><path d="M1 1l4 4-4 4M5 1l4 4-4 4" fill="none" stroke="#333" stroke-width="1.4"/></svg>Quisque imperdiet luctus tempus</li>
      <li><svg width="10" height="10" viewBox="0 0 10 10"><path d="M1 1l4 4-4 4M5 1l4 4-4 4" fill="none" stroke="#333" stroke-width="1.4"/></svg>Pellentesque quis purus</li>
    </ul>
    <span class="btn" style="margin-top:32px">Read More</span>
  </section>

  <section class="abs blog">
    <h3 class="col-title">Latest From Our Blog</h3>
    <div class="blog-photo" role="img" aria-label="Close-up of brightly coloured feathers"></div>
    <h3>Lorem ipsum dolor sit amet, consectetur.</h3>
    <p>Lorem ipsum dolor sit amet, consectetur adipiscing elit. Sed ornare sodales purus et dignissim. Morbi et purus sed dolor laoreet molestie a in dolor. In hac habitasse</p>
    <span class="btn" style="margin-top:20px">Read More</span>
  </section>

  <section class="abs tweets">
    <h3 class="col-title">Chirpline Feed</h3>
    <ul>
      <li>Lorem ipsum dolor sit amet, consectetur adipiscing elit. Sed ornare sodales purus et dignissim.<span class="link">http://drft.ly/wA165d</span></li>
      <li>Lorem ipsum dolor sit amet, consectetur adipiscing elit. Sed ornare sodales.<span class="link">http://drft.ly/wA1</span></li>
      <li>Lorem ipsum dolor sit amet, consectetur adipiscing elit. Sed ornare sodales purus.<span class="link">http://drft.ly/wd</span></li>
    </ul>
  </section>

  <div class="abs support">For live support click here! Or call us +00 000 000</div>

  <footer class="abs footer">
    <div class="abs f-col f-about">
      <h4>About Us</h4>
      <p>Lorem ipsum dolor sit amet, consectetur adipiscing elit. Sed ornare sodales purus et dignissim. Morbi et purus sed dolor laoreet molestie a in dolor. In hac habitasse platea dictumst. Pellentesque turpis eros, ornare quis malesuada nec, bibendum vel arcu. In egestas posuere ipsum a bibendum. Quisque imperdiet luctus tempus. Pellentesque quis purus.</p>
    </div>
    <div class="abs f-col f-news">
      <h4>Company News</h4>
      <ul>
        <li>›&nbsp; Lorem ipsum dolor sit amet</li>
        <li>›&nbsp; Sed ornare sodales purus</li>
        <li>›&nbsp; Morbi et purus sed dolor</li>
        <li class="hot">›&nbsp; In hac habitasse platea dictumst</li>
        <li>›&nbsp; Pellentesque turpis eros</li>
        <li>›&nbsp; In egestas posuere ipsum</li>
        <li>›&nbsp; Quisque imperdiet luctus tempus</li>
      </ul>
    </div>
    <div class="abs f-col f-posts">
      <h4>Latest Blog Posts</h4>
      <div class="f-post"><span class="thumb"><svg width="22" height="16" viewBox="0 0 22 16"><rect x="1" y="3" width="20" height="12" rx="2" fill="#8a8a8a"/><circle cx="11" cy="9" r="4" fill="#686868"/><rect x="7" y="0" width="8" height="4" fill="#8a8a8a"/></svg></span><p class="hot">Lorem ipsum dolor sit amet, consectetur.<em>15. March 2015</em></p></div>
      <div class="f-post"><span class="thumb"><svg width="22" height="16" viewBox="0 0 22 16"><rect x="1" y="3" width="20" height="12" rx="2" fill="#8a8a8a"/><circle cx="11" cy="9" r="4" fill="#686868"/><rect x="7" y="0" width="8" height="4" fill="#8a8a8a"/></svg></span><p>Lorem ipsum dolor sit amet, consectetur.<em>19. March 2015</em></p></div>
      <div class="f-post"><span class="thumb"><svg width="22" height="16" viewBox="0 0 22 16"><rect x="1" y="3" width="20" height="12" rx="2" fill="#8a8a8a"/><circle cx="11" cy="9" r="4" fill="#686868"/><rect x="7" y="0" width="8" height="4" fill="#8a8a8a"/></svg></span><p>Lorem ipsum dolor sit amet, consectetur.<em>21. April 2015</em></p></div>
    </div>
    <div class="abs f-col f-contact">
      <h4>Contact Us</h4>
      <div class="field first">Your Name</div>
      <div class="field">E-mail</div>
      <div class="field msg">Message</div>
      <div class="send">SEND</div>
    </div>
  </footer>

  <div class="abs social-bar">
    <h4>Stay Connected With Us</h4>
    <div class="socials">
      <span><i></i>Chirpline</span>
      <span><i></i>Friendwall</span>
      <span><i></i>WorkLinks</span>
      <span><i></i>RSS</span>
      <span><i></i>Shotboard</span>
      <span><i></i>Circleplus</span>
    </div>
  </div>
  <div class="abs copyright">Copyright @driftwood coatings LLC. All rights reserved</div>

</div>
</body>
</html>
```